Book Cover in a 6x9 inches size for BEFORE THE LANTERNS FADE

Instructions for creating a 6x9 inches book cover to be uploaded on PressVellum:
1. I am not sure what I want for a book cover. Hope you can put your
creative mind to work to think of something unique and creative as a
book cover with the photos I've provided ☺
2. Let me explain a bit so that you understand what the book is about:
The Title: BEFORE THE LANTERNS FADE.
The title comes from the Bible verse Luke 19:37-40 about Jesus’ last
ride into Jerusalem before His crucifixion, when a multitude of
disciples were rejoicing and praising God for all the mighty works that
they had seen. The Pharisees (who were the religious authorities of the
Jews) said to Jesus: “Master, rebuke thy disciples”. He said unto them: “I
tell you that, if these should hold their peace, the stones would
immediately cry out.”
It really means when people who were created by Almighty God do not
want to praise and worship Him, creation will, as mentioned in different
sections in the Bible. In this particular verse Jesus said if the people are
not going to praise Him, the stones will. It came from a time that I was
sad to see how few people at my workplace wanted to know about God,
let alone serve Him. The Bible verses painted on the river stones are
about my stone ministry that I’ve started on earth. This is a symbol of
when God’s people do not want to praise Him, I’ll make sure the stones
will cry out, resembling what Jesus said in Luke 19:37-40. I use Bible
verses to praise God, to break the curses on the land, for protection, and
for blessings.
2. I have uploaded 3 preferred photos (that were edited and the colors
enhanced) which I think will work best. But I also uploaded three other
photos which were not edited if you think that you can use them to help
your creation idea. The one photo of the stones that have enough white
space between them was taken with the idea if you want to have it
separated to make your own design.
3. The main aim is for people to see how the painted stones look like that I
use in my stone ministry. When they read the ‘Forward’ of the book it
will be clear what the meaning of the painted stones on the book cover
is.
4. I am looking forward to receive a beautiful book cover. Do not hesitate
to send me a message if you have any questions or need clarification.
Thank you 😊
Christians

```html
<!DOCTYPE html>
<html lang="en">
<head>
<meta charset="utf-8">
<title>Before the Lanterns Fade — Book Cover</title>
<link rel="stylesheet" href="https://fonts.googleapis.com/css2?family=Poppins:wght@700&family=Fredoka:wght@700&family=Libre+Baskerville:wght@700&display=swap">
<style>
  :root {
    --aqua-light: #dcf8f1;
    --aqua-mid: #bdeee2;
    --aqua-deep: #a6e6d6;
    --ink: #161616;
    --title-red: #e34a1c;
    --title-edge: #8a2a10;
    --stone-dark: #5f554d;
    --stone-mid: #a08a7a;
    --stone-light: #c9b8a8;
  }
  html, body {
    margin: 0;
    padding: 0;
    overflow: hidden;
    background: #ffffff;
  }
  .cover {
    position: relative;
    width: 800px;
    height: 1200px;
    overflow: hidden;
    background:
      radial-gradient(ellipse at 30% 20%, var(--aqua-light) 0%, transparent 55%),
      radial-gradient(ellipse at 75% 60%, var(--aqua-light) 0%, transparent 50%),
      linear-gradient(180deg, var(--aqua-mid) 0%, var(--aqua-deep) 45%, var(--aqua-mid) 100%);
  }
  .author {
    position: absolute;
    top: 59px;
    left: 0;
    width: 100%;
    margin: 0;
    text-align: center;
    font-family: "Poppins", sans-serif;
    font-weight: 700;
    font-size: 38px;
    line-height: 1;
    letter-spacing: 7px;
    color: var(--ink);
  }
  .title {
    position: absolute;
    top: 140px;
    left: 0;
    width: 100%;
    margin: 0;
    text-align: center;
    font-family: "Fredoka", sans-serif;
    font-weight: 700;
    font-size: 112px;
    line-height: 112px;
    letter-spacing: 0;
    color: var(--title-red);
    text-shadow: 0 0 1px var(--title-edge), 0 1px 0 var(--title-edge);
  }
  .title span { display: block; white-space: nowrap; }
  .subtitle {
    position: absolute;
    top: 512px;
    left: 20px;
    width: 760px;
    margin: 0;
    text-align: center;
    font-family: "Libre Baskerville", serif;
    font-weight: 700;
    font-size: 25.5px;
    line-height: 46px;
    color: var(--ink);
  }
  .stones {
    position: absolute;
    left: 0;
    top: 680px;
    width: 800px;
    height: 520px;
  }
</style>
</head>
<body>
  <main class="cover">
    <p class="author">MARA VANDELEUR</p>
    <h1 class="title">
      <span>BEFORE THE</span>
      <span>LANTERNS</span>
      <span>FADE</span>
    </h1>
    <p class="subtitle">The importance of worshipping God,<br>And End Time Prophecies to help you prepare<br>for the Rapture and Return of Jesus Christ.</p>
    <svg class="stones" viewBox="0 0 800 520" role="img" aria-label="Photograph of a heap of smooth river stones, several painted with white Bible verse references, scattered with water droplets">
      <defs>
        <radialGradient id="stone-heap" cx="50%" cy="55%" r="60%">
          <stop offset="0%" stop-color="#c9b8a8"/>
          <stop offset="55%" stop-color="#a08a7a"/>
          <stop offset="100%" stop-color="#5f554d"/>
        </radialGradient>
      </defs>
      <path d="M0 520 L0 300 C40 260 90 200 170 160 C240 110 300 30 400 20 C500 15 560 60 620 110 C700 170 760 240 800 290 L800 520 Z" fill="url(#stone-heap)"/>
    </svg>
  </main>
</body>
</html>
```